Business Card for Amber Heron Advisors

Business card design for Amber Heron Advisors, a new consulting and financial advisory firm. I would like the designs to integrate the logo attached (at least on 1 side).

Target Market(s)

individual and institutional clients

Contact Information for Business Card

Dominic L. Hartwell, CFA
Managing Director
amberheronadvisors.examplep
hartwell@amberheronadvisors.example
(555) 218-4903

```html
<!DOCTYPE html>
<html lang="en">
<head>
<meta charset="utf-8">
<title>Amber Heron Advisors — Business Card</title>
<link rel="stylesheet" href="https://fonts.googleapis.com/css2?family=Arimo:wght@400;700&display=swap">
<style>
  :root {
    --stage: #2e2e2e;
    --paper: #ffffff;
    --paper-shade: #ececec;
    --ink-dark: #242424;
    --amber: #d97a1e;
    --light-text: #e6e6e6;
  }
  * { margin: 0; padding: 0; box-sizing: border-box; }
  html, body {
    width: 1200px; height: 997px; overflow: hidden;
    background: var(--stage);
    font-family: "Arimo", Arial, sans-serif;
  }
  .stage {
    width: 1200px; height: 997px;
    display: flex; flex-direction: column;
    align-items: center; justify-content: center; gap: 60px;
  }
  .card {
    position: relative;
    width: 560px; height: 320px;
    border-radius: 18px; overflow: hidden;
    background: linear-gradient(160deg, var(--paper) 40%, var(--paper-shade));
    box-shadow: 0 14px 30px rgba(0,0,0,.45);
  }
  .wordmark {
    color: var(--amber);
    font-weight: 700;
    letter-spacing: 1px;
    text-transform: uppercase;
    white-space: nowrap;
  }
  .card-front { display: flex; align-items: center; justify-content: center; }
  .card-front .wordmark { font-size: 34px; }

  .card-back .top {
    position: absolute; left: 0; right: 0; top: 0; height: 150px;
    display: flex; align-items: center; justify-content: center;
  }
  .card-back .wordmark { font-size: 26px; }
  .card-back .rule {
    position: absolute; left: 0; right: 0; top: 150px; height: 4px;
    background: var(--amber);
  }
  .card-back .bottom {
    position: absolute; left: 0; right: 0; top: 154px; bottom: 0;
    background: var(--ink-dark);
  }
  .card-back .notch {
    position: absolute; left: 26px; top: 0; width: 22px; height: 12px;
  }
  .holder { position: absolute; left: 32px; top: 24px; }
  .holder .name { color: var(--amber); font-size: 19px; }
  .holder .role { color: var(--light-text); font-size: 11px; margin-top: 5px; }
  .contacts { position: absolute; left: 32px; bottom: 24px; list-style: none; }
  .contacts li {
    display: flex; align-items: center; gap: 10px;
    color: var(--light-text); font-size: 13px; margin-top: 7px;
  }
  .contacts svg { width: 12px; height: 12px; fill: var(--amber); }
  .website {
    position: absolute; right: 28px; top: 40px;
    color: var(--amber); font-size: 14px; font-weight: 700;
  }
</style>
</head>
<body>
<main class="stage">
  <section class="card card-front" aria-label="Card front">
    <span class="wordmark">Amber Heron Advisors</span>
  </section>

  <section class="card card-back" aria-label="Card back">
    <div class="top"><span class="wordmark">Amber Heron Advisors</span></div>
    <div class="rule"></div>
    <div class="bottom">
      <svg class="notch" viewBox="0 0 22 12"><polygon points="0,0 22,0 11,12" fill="#d97a1e"/></svg>
      <div class="holder">
        <p class="name">Dominic L. Hartwell, CFA</p>
        <p class="role">Managing Director</p>
      </div>
      <p class="website">www.amberheronadvisors.example</p>
      <ul class="contacts">
        <li>
          <svg viewBox="0 0 24 24" aria-hidden="true"><path d="M6.6 10.8a15 15 0 0 0 6.6 6.6l2.2-2.2a1 1 0 0 1 1-.25 11.4 11.4 0 0 0 3.6.57 1 1 0 0 1 1 1V20a1 1 0 0 1-1 1A17 17 0 0 1 3 4a1 1 0 0 1 1-1h3.5a1 1 0 0 1 1 1c0 1.25.2 2.45.57 3.57a1 1 0 0 1-.25 1z"/></svg>
          (555) 218-4903
        </li>
        <li>
          <svg viewBox="0 0 24 24" aria-hidden="true"><path d="M2 5h20v14H2zM4 7v.5l8 5 8-5V7l-8 5z"/></svg>
          hartwell@amberheronadvisors.example
        </li>
      </ul>
    </div>
  </section>
</main>
</body>
</html>
```